Business card for massage therapy company called Brook Fern Wellness

Need business card for massage therapy company called Brook Fern Wellness. Would like my logo on the front and the back of the card I have 3 options of logos and you can play with what looks better.

Would like this information displayed on the back of the card:

Marcus Ellery
Licensed Massage Therapist
321-555-0147
brookfern-example.com
brookfern_rest_

```html
<!DOCTYPE html>
<html lang="en">
<head>
<meta charset="utf-8">
<title>Brook Fern Wellness — Business Card</title>
<link rel="stylesheet" href="https://fonts.googleapis.com/css2?family=Poppins:wght@300;400&family=Marcellus&display=swap">
<style>
  :root {
    --sage: #737a62;
    --sage-text: #5f6552;
    --clay: #c0957a;
    --paper: #ffffff;
    --backdrop: #ebe7e1;
    --faint: #f3f3f1;
  }
  * { box-sizing: border-box; margin: 0; padding: 0; }
  html, body {
    width: 1189px; height: 1200px; overflow: hidden;
    background: var(--backdrop);
    font-family: "Poppins", sans-serif;
  }
  .canvas { position: relative; width: 1189px; height: 1200px; }
  .card {
    position: absolute; left: 170px; width: 850px; height: 484px;
    border-radius: 34px; overflow: hidden;
    box-shadow: 0 6px 18px rgba(0,0,0,0.18);
  }
  .card-front { top: 112px; background: var(--sage); }
  .card-back { top: 641px; background: var(--paper); }

  .front-mark {
    position: absolute; inset: 0;
    display: flex; align-items: center; justify-content: center; gap: 22px;
  }
  .front-mark .ring {
    width: 58px; height: 58px; border: 2px solid var(--paper); border-radius: 50%;
  }
  .front-mark .brand-name {
    color: var(--paper); font-weight: 300; font-size: 40px; letter-spacing: 2px;
  }

  .faint-ring {
    position: absolute; left: 395px; top: -30px;
    width: 400px; height: 400px; border: 3px solid var(--faint); border-radius: 50%;
  }
  .back-brand {
    position: absolute; left: 51px; top: 95px;
    color: var(--sage-text); font-weight: 300; font-size: 46px; line-height: 1.1;
  }
  .holder-name {
    position: absolute; left: 51px; top: 288px;
    font-family: "Marcellus", serif; font-size: 30px; letter-spacing: 1px;
    color: var(--sage-text);
  }
  .holder-role {
    position: absolute; left: 51px; top: 322px;
    font-size: 19px; font-weight: 300; color: var(--clay);
  }
  .rule {
    position: absolute; left: 51px; top: 354px; width: 750px; height: 2px;
    background: var(--clay);
  }
  .contact {
    position: absolute; left: 51px; list-style: none;
    display: flex; align-items: center; gap: 10px;
    font-size: 20px; font-weight: 300; color: var(--sage-text);
  }
  .contact.phone { top: 373px; }
  .contact.web { top: 405px; }
  .contact svg { width: 26px; height: 26px; }

  .band-clay {
    position: absolute; left: 0; top: 463px; width: 455px; height: 22px;
    background: var(--clay); clip-path: polygon(0 0, 100% 0, 98% 100%, 0 100%);
  }
  .band-sage {
    position: absolute; left: 462px; top: 439px; width: 388px; height: 46px;
    background: var(--sage); clip-path: polygon(5% 0, 100% 0, 100% 100%, 0 100%);
  }
  .handle {
    position: absolute; left: 548px; top: 446px;
    color: var(--paper); font-size: 20px; letter-spacing: 1px;
  }
</style>
</head>
<body>
<main class="canvas">
  <section class="card card-front">
    <div class="front-mark">
      <span class="ring"></span>
      <span class="brand-name">Brook Fern Wellness</span>
    </div>
  </section>

  <section class="card card-back">
    <span class="faint-ring"></span>
    <h1 class="back-brand">Brook Fern Wellness</h1>
    <p class="holder-name">MARCUS ELLERY</p>
    <p class="holder-role">Licensed Massage Therapist</p>
    <span class="rule"></span>
    <ul>
      <li class="contact phone">
        <svg viewBox="0 0 26 26" aria-hidden="true">
          <circle cx="13" cy="13" r="13" fill="#737a62"/>
          <rect x="8.5" y="6" width="9" height="14" rx="1.5" fill="none" stroke="#fff" stroke-width="1.6"/>
          <line x1="11" y1="17.5" x2="15" y2="17.5" stroke="#fff" stroke-width="1.4"/>
        </svg>
        321-555-0147
      </li>
      <li class="contact web">
        <svg viewBox="0 0 26 26" aria-hidden="true">
          <circle cx="13" cy="13" r="13" fill="#737a62"/>
          <rect x="6.5" y="8.5" width="13" height="9" rx="1" fill="none" stroke="#fff" stroke-width="1.5"/>
          <polyline points="6.5,8.5 13,13.5 19.5,8.5" fill="none" stroke="#fff" stroke-width="1.5"/>
        </svg>
        brookfern-example.com
      </li>
    </ul>
    <span class="band-clay"></span>
    <span class="band-sage"></span>
    <p class="handle">brookfern_rest_</p>
  </section>
</main>
</body>
</html>
```